Need a sleek, professional business card design for a Web Development business

I need a unique business card designed for a web development company. It is also the parent company for any ventures I do, such as my ClipWave channel, startup ideas I have, etc. I am the single member of "Bright Harbor Code LLC." I will attach my basic logo here, so you will see the current color scheme and have the asset available. Thank you!

Target Market(s)

Startups, SMB's, Professionals

Industry/Entity Type

Business

Font styles to use
Other font styles liked:
• Lovello for headings is what I use, but not necessary.

Colors

Designer to choose colors to be used in the design.

Requirements
Nice to have
• Sleek is the word. Professional, modern, dark.
Should not have
• Any work from someone else's design. Lacking originality.

```html
<!DOCTYPE html>
<html lang="en">
<head>
<meta charset="utf-8">
<title>Bright Harbor Code LLC — Business Card</title>
<link rel="stylesheet" href="https://fonts.googleapis.com/css2?family=Open+Sans:wght@400;700&display=swap">
<style>
  :root {
    --backdrop: #2a2726;
    --card-orange: #f5a05e;
    --card-black: #161616;
    --card-strip: #454545;
    --mark-dark: #1f1f1f;
    --ink: #111111;
    --contact-text: #f2f2f2;
    --icon-gold: #e5a13a;
  }
  * { margin: 0; padding: 0; box-sizing: border-box; }
  html, body {
    width: 1200px;
    height: 716px;
    overflow: hidden;
    background: var(--backdrop);
    font-family: "Open Sans", Arial, sans-serif;
  }
  .card {
    position: absolute;
    left: 80px;
    top: 61px;
    width: 1040px;
    height: 594px;
    background: var(--card-orange);
    overflow: hidden;
  }
  .brand {
    position: absolute;
    right: 90px;
    top: 150px;
    display: flex;
    flex-direction: column;
    align-items: flex-end;
  }
  .brand-square {
    width: 180px;
    height: 180px;
    border-radius: 16px;
    background: var(--mark-dark);
    margin-right: 40px;
  }
  .brand-name {
    margin-top: 14px;
    font-weight: 700;
    font-size: 32px;
    color: var(--ink);
    letter-spacing: 0.3px;
  }
  .contact-band {
    position: absolute;
    left: 0;
    top: 400px;
    width: 100%;
    height: 160px;
    background: var(--card-black);
  }
  .contact-strip {
    position: absolute;
    left: 0;
    bottom: 0;
    width: 100%;
    height: 34px;
    background: var(--card-strip);
  }
  .contact-list {
    position: absolute;
    list-style: none;
    color: var(--contact-text);
    font-size: 19px;
    line-height: 30px;
  }
  .contact-list li { display: flex; align-items: center; gap: 10px; }
  .contact-list svg { width: 18px; height: 18px; flex: none; }
  .contact-left { left: 40px; top: 24px; }
  .contact-right { right: 60px; top: 38px; }
</style>
</head>
<body>
  <main class="card">
    <div class="brand">
      <div class="brand-square"></div>
      <div class="brand-name">Bright Harbor Code LLC</div>
    </div>

    <section class="contact-band">
      <ul class="contact-list contact-left">
        <li>
          <svg viewBox="0 0 20 20" aria-hidden="true"><path fill="var(--icon-gold)" d="M10 1a6 6 0 0 0-6 6c0 4.5 6 12 6 12s6-7.5 6-12a6 6 0 0 0-6-6zm0 8.5A2.5 2.5 0 1 1 10 4.5a2.5 2.5 0 0 1 0 5z"/></svg>
          2718 Harbor View Ave, Suite 120, Tacoma, WA 98402
        </li>
        <li>
          <svg viewBox="0 0 20 20" aria-hidden="true"><rect x="2" y="7" width="16" height="10" rx="2" fill="var(--icon-gold)"/><rect x="5" y="3" width="10" height="5" fill="var(--icon-gold)"/><rect x="5" y="10" width="10" height="2" fill="var(--card-black)"/></svg>
          555.310.4472
        </li>
        <li>
          <svg viewBox="0 0 20 20" aria-hidden="true"><rect x="2" y="4" width="16" height="12" rx="1.5" fill="none" stroke="var(--icon-gold)" stroke-width="2"/><path d="M2.5 5 10 11l7.5-6" fill="none" stroke="var(--icon-gold)" stroke-width="2"/></svg>
          sam@brightharborcode.com
        </li>
      </ul>

      <ul class="contact-list contact-right">
        <li>
          <svg viewBox="0 0 20 20" aria-hidden="true"><path fill="var(--icon-gold)" d="M5 2h3l1.5 4-2 1.5a10 10 0 0 0 5 5l1.5-2 4 1.5v3a2 2 0 0 1-2 2A15 15 0 0 1 3 4a2 2 0 0 1 2-2z"/></svg>
          555.310.4470
        </li>
        <li>
          <svg viewBox="0 0 20 20" aria-hidden="true"><rect x="5" y="1" width="10" height="18" rx="2" fill="var(--icon-gold)"/><rect x="7" y="4" width="6" height="10" fill="var(--card-black)"/></svg>
          555.862.0193
        </li>
        <li>
          <svg viewBox="0 0 20 20" aria-hidden="true"><circle cx="10" cy="10" r="8" fill="none" stroke="var(--icon-gold)" stroke-width="2"/><path d="M2 10h16M10 2c-3 3-3 13 0 16M10 2c3 3 3 13 0 16" fill="none" stroke="var(--icon-gold)" stroke-width="1.5"/></svg>
          www.brightharborcode.com
        </li>
      </ul>
    </section>

    <div class="contact-strip"></div>
  </main>
</body>
</html>
```